NimbusFern cyber security firm Website

We did our website ourselves on Joomla, it's not great. We want a wordpress based redesign. Some thing that will represent a modern cyber security firm that's aimed at solving business problems.
Https://nimbusfern.co.nz (current site)
#58427c - primary color (you'll know why when you see it's name)
Logo files can be provided. Ask for more info if you need.

We want a modern, quick to load website. Website is going to have a home - services - products - about us - blogs menu. Will need a footer menu, site map, contact page etc.
We getting Content done sperately.
Our logo is #58427c - so hoping for a light theme (or at least the top is).
While we have been specific around the color - we are not after a website that has too much of it.

Reference sites that we like :
https://www.voltaline.co.nz/ - Love the full screen real world image
https://wardvex.co.nz/ (love the real world imagry and motion)
https://www.qtr.com/us-en?lnk=m
https://redowlen.com

Please dont use :
cartoon or redered images : (Like this : https://img.stockmorra.com/free-vector/cyber-security-concept_23-2148543851.jpg?w=2000 )

Please don't use images like this : https://www.tavelundi.com/eu/blog/oil-gas/app/uploads/2020/04/116137226_s-1440x564_c.jpg - they are old and boring.

We would like to see some creativity - loading our logo into a readymade wordpress template and hitting go won't cut it.
Updates

Thanks everyone who has submitted so far. We've extended the deadline as we wanted to give everyone a chance to Re- read the brief and perhaps make some tweeks should they feel it necessary.

Target Market(s)

Mid - large enterprise, finance, insurance, utilities vertical

Industry/Entity Type

Cyber security

Coding

Coded - Design and coding required

Number of Pages Required

5+ page

Font styles to use
Other font styles liked:
• Open sans

Colors

Designer to choose colors to be used in the design.

Requirements
Must have
• Simple clear messaging, something that catches user engagement
Nice to have
• Motion of some sort, but not overdone, GDPR

```html
<!DOCTYPE html>
<html lang="en">
<head>
<meta charset="utf-8">
<title>NimbusFern – Cyber Security</title>
<link href="https://fonts.googleapis.com/css2?family=Open+Sans:wght@400;500;600;700&family=Roboto:wght@400&display=swap" rel="stylesheet">
<style>
:root{
  --brand:#58427c;
  --brand-soft:#6a5590;
  --ink:#222;
  --admin:#1d2327;
  --admin-text:#f0f0f1;
  --band:#f2f2f2;
  --line:#d9d9d9;
  --hero-top:#66757c;
  --hero-mid:#3c5a3a;
  --hero-low:#2f5872;
  --hero-deep:#1f4058;
  --partner-a:#1f7fa8;
  --partner-b:#3fbf6a;
}
*{box-sizing:border-box;margin:0;padding:0}
html,body{width:685px;height:1200px;overflow:hidden;background:#fff}
body{position:relative;font-family:"Open Sans",sans-serif;color:var(--ink)}
a{color:inherit;text-decoration:none}

.admin-bar{position:absolute;top:0;left:0;width:685px;height:18px;background:var(--admin);color:var(--admin-text);font-family:Roboto,sans-serif;font-size:6.5px;display:flex;align-items:center;padding:0 8px}
.admin-bar span{margin-right:10px}
.admin-bar .right{margin-left:auto;display:flex;align-items:center;gap:4px}
.admin-bar .avatar{width:8px;height:8px;background:#ccc;display:inline-block}

.top-strip{position:absolute;top:18px;left:0;width:685px;height:22px;border-bottom:1px solid var(--line);font-size:5px;font-weight:700}
.top-strip .contact{position:absolute;left:20px;top:0;height:22px;border-left:1px solid var(--ink);border-right:1px solid var(--ink);padding:0 11px;display:flex;align-items:center;gap:11px}
.top-strip .social{position:absolute;right:20px;top:0;display:flex;height:22px}
.top-strip .social span{width:21px;height:22px;border-left:1px solid var(--ink);display:flex;align-items:center;justify-content:center}
.top-strip .social span:last-child{border-right:1px solid var(--ink)}
.top-strip .social i{width:4px;height:4px;border-radius:50%;background:var(--ink);display:block}

.site-header{position:absolute;top:40px;left:0;width:685px;height:55px}
.brand-name{position:absolute;left:26px;top:14px;font-size:24px;font-weight:600;color:var(--brand);letter-spacing:.5px;display:flex;align-items:center;gap:7px}
.brand-name i{width:22px;height:22px;border-radius:50%;background:var(--brand);display:block}
.main-nav{position:absolute;right:28px;top:22px;display:flex;gap:17px;font-size:9px;font-weight:500;letter-spacing:1.2px;color:var(--brand)}

.hero{position:absolute;top:95px;left:0;width:685px;height:303px;background:
  radial-gradient(ellipse 70% 35% at 55% 40%,rgba(52,90,40,.9),rgba(52,90,40,0) 70%),
  linear-gradient(180deg,var(--hero-top) 0%,#5a6b62 22%,var(--hero-mid) 40%,var(--hero-low) 50%,var(--hero-deep) 100%)}
.hero h1{position:absolute;left:57px;top:148px;color:#fff;font-size:32px;font-weight:500}
.hero p{position:absolute;left:57px;top:197px;width:360px;color:#fff;font-size:12px;line-height:15.5px}

.section-title{position:absolute;top:450px;left:285px;width:114px;border-top:1px solid var(--line);border-bottom:1px solid var(--line);text-align:center;padding:6px 0 5px;color:var(--brand);font-size:17px;font-weight:600}

.services{position:absolute;top:550px;left:12px;width:661px;display:flex}
.service{width:132px;text-align:center;position:relative;height:200px}
.service .photo{width:69px;height:69px;border-radius:50%;margin:0 auto}
.photo.vciso{background:radial-gradient(circle at 40% 45%,#d98a4a 0%,#8a4a2a 40%,#2c211d 100%)}
.photo.assess{background:radial-gradient(circle at 60% 40%,#3fb4d8 0%,#1d5f8a 45%,#0f2233 100%)}
.photo.thirdparty{background:linear-gradient(180deg,#4c6a85 0%,#8a97a3 45%,#d7d7d2 70%,#3b3b3b 100%)}
.photo.human{background:linear-gradient(180deg,#b9c2c9 0%,#8d8579 45%,#6b6a50 75%,#4a4a3a 100%)}
.photo.warrant{background:radial-gradient(circle at 55% 55%,#3c8bb0 0%,#1f4a66 45%,#0f1e2b 100%)}
.service h3{width:108px;margin:17px auto 0;font-size:11.5px;font-weight:500;color:var(--brand-soft);line-height:15.5px}
.service p{width:122px;margin:4px auto 0;font-size:9px;line-height:18.5px}
.service p.narrow{width:100px}
.service .more{position:absolute;left:0;right:0;top:184px;font-size:6px;font-weight:700;letter-spacing:2.6px;color:var(--brand)}
.service .more.low{top:188px}

.contact-band{position:absolute;top:779px;left:0;width:685px;height:105px;background:var(--band)}
.contact-item{position:absolute;top:30px}
.contact-item svg{position:absolute;left:0;top:12px}
.contact-item strong{position:absolute;left:45px;top:0;font-size:11.5px;font-weight:400;color:var(--brand);white-space:nowrap}
.contact-item span{position:absolute;left:45px;top:24px;font-size:9px;white-space:nowrap}

.footer{position:absolute;top:884px;left:0;width:685px;height:250px}
.footer .col{position:absolute;top:36px}
.footer h4{font-size:11.5px;font-weight:500;color:var(--brand-soft);margin-bottom:14px}
.footer ul{list-style:none;font-size:9px;line-height:22px}
.footer .about-name{font-size:14px;font-weight:600;color:var(--brand);display:flex;align-items:center;gap:6px}
.footer .about-name i{width:12px;height:12px;border-radius:50%;background:var(--brand);display:block}
.footer .about-text{margin-top:36px;width:135px;font-size:9px;line-height:19px}
.badge-a{margin-top:40px;width:56px;height:50px;border-radius:50%;background:var(--partner-a);opacity:.85}
.badge-b{margin-top:40px;width:132px;height:34px;border-radius:17px;background:var(--partner-b);opacity:.8}

.bottom-bar{position:absolute;top:1134px;left:0;width:685px;height:66px;background:var(--band);text-align:center}
.bottom-bar .copy{margin-top:20px;font-size:5px;font-weight:700}
.bottom-bar nav{margin-top:19px;font-size:5px;font-weight:700;color:var(--brand);display:flex;justify-content:center;gap:18px}
.up{position:absolute;right:14px}
</style>
</head>
<body>

<div class="admin-bar">
  <span>NimbusFern</span><span>Customize</span><span>3</span><span>0</span><span>+ New</span><span>Edit Page</span><span>Edit with PageForge Page Builder</span>
  <div class="right">Howdy, admin <i class="avatar"></i></div>
</div>

<div class="top-strip">
  <div class="contact"><span>PHONE : +64 (0) 210 555 0142</span><span>EMAIL :INFO@NIMBUSFERN.CO.NZ</span></div>
  <div class="social">
    <span><svg width="7" height="7" viewBox="0 0 10 10"><circle cx="4" cy="4" r="3" fill="none" stroke="#222" stroke-width="1"/><line x1="6.2" y1="6.2" x2="9" y2="9" stroke="#222"/></svg></span>
    <span><i></i></span><span><i></i></span><span><i></i></span>
  </div>
</div>

<header class="site-header">
  <div class="brand-name"><i></i>NIMBUSFERN</div>
  <nav class="main-nav"><a>HOME</a><a>SERVICES</a><a>PRODUCTS</a><a>ABOUT US</a><a>BLOG</a></nav>
</header>

<section class="hero" role="img" aria-label="Photograph of a forested mountain rising above a deep blue lake">
  <h1>NimbusFern?</h1>
  <p>NimbusFern is a 100% New Zealand owned and operated cyber security company, providing cyber risk mitigation and management solutions to all businesses.</p>
</section>

<h2 class="section-title">WHAT WE DO</h2>

<section class="services">
  <div class="service"><div class="photo vciso" role="img" aria-label="Photo of hands holding a phone with glowing security icons"></div><h3>Virtual CISO</h3><p class="narrow">The vCISO is a security practitioner to help organizations</p><a class="more low">READ MORE &gt;&gt;&gt;</a></div>
  <div class="service"><div class="photo assess" role="img" aria-label="Photo of hands typing on a laptop with glowing padlocks"></div><h3>Cyber Risk Assessment</h3><p>Cyber Threat Susceptibility Assessment</p><a class="more">READ MORE &gt;&gt;&gt;</a></div>
  <div class="service"><div class="photo thirdparty" role="img" aria-label="Photo of a laptop keyboard with the word risk on screen"></div><h3>Third-party Risk Management</h3><p>Strongest Weapon Against Data Loss</p><a class="more">READ MORE &gt;&gt;&gt;</a></div>
  <div class="service"><div class="photo human" role="img" aria-label="Photo of a wooden signpost reading risk, control, management"></div><h3>Human Risk Management</h3><p>Transform employees into your first line of defence</p><a class="more">READ MORE &gt;&gt;&gt;</a></div>
  <div class="service"><div class="photo warrant" role="img" aria-label="Photo of hands on a keyboard with security overlays"></div><h3>Cyber Security Warrant of Fitness</h3><p>Cyber Security Warrant of Fitness</p><a class="more">READ MORE &gt;&gt;&gt;</a></div>
</section>
<svg class="up" style="top:653px" width="12" height="7" viewBox="0 0 14 8"><polyline points="1,7 7,1 13,7" fill="none" stroke="#222" stroke-width="1"/></svg>

<section class="contact-band">
  <div class="contact-item" style="left:30px">
    <svg width="20" height="22" viewBox="0 0 20 22"><path d="M6 3 L3 4 C1 9 3 16 7 19 L10 17 L8 13 L6 14 C5 12 5 9 5 8 L7 7 Z" fill="var(--brand)"/><path d="M11 6 A4 4 0 0 1 11 12 M13 4 A7 7 0 0 1 13 14" fill="none" stroke="var(--brand)" stroke-width="1.3"/></svg>
    <strong>+64 (0) 210 555 0142</strong><span>Call Us</span>
  </div>
  <div class="contact-item" style="left:248px">
    <svg width="22" height="18" viewBox="0 0 22 18"><rect x="1" y="1" width="20" height="16" rx="1" fill="none" stroke="var(--brand)" stroke-width="1.5"/><polyline points="1,2 11,10 21,2" fill="none" stroke="var(--brand)" stroke-width="1.5"/></svg>
    <strong>info@nimbusfern.co.nz</strong><span>Email Us</span>
  </div>
  <div class="contact-item" style="left:469px">
    <svg width="20" height="20" viewBox="0 0 20 20"><circle cx="10" cy="10" r="8.5" fill="none" stroke="var(--brand)" stroke-width="1.8"/><polyline points="10,5 10,11 6,11" fill="none" stroke="var(--brand)" stroke-width="1.8"/></svg>
    <strong>info@nimbusfern.co.nz</strong><span>Email Us</span>
  </div>
  <svg class="up" style="top:60px" width="12" height="7" viewBox="0 0 14 8"><polyline points="1,7 7,1 13,7" fill="none" stroke="#222" stroke-width="1"/></svg>
</section>

<footer class="footer">
  <div class="col" style="left:20px;top:38px">
    <div class="about-name"><i></i>NIMBUSFERN</div>
    <p class="about-text">NimbusFern is a 100% New Zealand owned and operated cyber security company,</p>
  </div>
  <div class="col" style="left:185px">
    <h4>Company</h4>
    <ul><li>About Us</li><li>Our Founders</li><li>Legal Information</li><li>Blog</li><li>Contact Us</li></ul>
  </div>
  <div class="col" style="left:350px">
    <h4>Capabilities</h4>
    <ul><li>Human Risk Management</li><li>Managed Third-Party Cyber Risk</li><li>Third Party Risk Management</li><li>Vulnerability Management</li><li>Vaultly Password Management</li><li>Stratocloud – Cloud Based Security</li></ul>
  </div>
  <div class="col" style="left:515px">
    <h4>Partners</h4>
    <div class="badge-a" role="img" aria-label="Networking partner certification badge"></div>
    <div class="badge-b" role="img" aria-label="Risk intelligence partner badge"></div>
  </div>
</footer>

<div class="bottom-bar">
  <p class="copy">COPYRIGHT 2022 -NIMBUSFERN ALL RIGHTS RESERVED.</p>
  <nav><a>SITE MAP</a><a>LEGAL INFORMATION</a></nav>
  <svg class="up" style="top:40px" width="12" height="7" viewBox="0 0 14 8"><polyline points="1,7 7,1 13,7" fill="none" stroke="#222" stroke-width="1"/></svg>
</div>

</body>
</html>
```